We have a company that provide sandblasted stone products. Example: numbers for houses. Also we sell cultured stone,brick natural stone to the contractor,homeowner. We need to get a business card that describe our product and service. In the original idea we had an old fashion chisel striking through the x in quelvadine.
Updates

Reason: We realized that 2 days was not enough time for the competion to be open many of the designers may be to busy and require more time to compete.

Industry/Entity Type

It Company

Logo Text

Quelvadine

```html
<!DOCTYPE html>
<html lang="en">
<head>
<meta charset="utf-8">
<title>Quelvadine Business Card</title>
<link rel="stylesheet" href="https://fonts.googleapis.com/css2?family=Bebas+Neue&family=Open+Sans:wght@400&display=swap">
<style>
  :root {
    --page: #ffffff;
    --stone: #efe2c7;
    --stone-light: #f6ead2;
    --edge: #8a8a8a;
    --band-light: #8f8f91;
    --band-dark: #3a3a3c;
    --band-charcoal: #333335;
    --ink: #000000;
    --muted: #6d6e71;
    --icon: #ffffff;
  }
  * { margin: 0; padding: 0; box-sizing: border-box; }
  html, body { width: 1200px; height: 1000px; overflow: hidden; background: var(--page); }
  .canvas { position: relative; width: 1200px; height: 1000px; }

  .card {
    position: absolute;
    width: 300px;
    height: 526px;
    border: 1px solid var(--edge);
    overflow: hidden;
  }
  .card--front { left: 201px; top: 214px; }
  .card--back  { left: 552px; top: 294px; }

  .card__texture {
    position: absolute; inset: 0;
    background: radial-gradient(ellipse at 45% 50%, var(--stone-light), var(--stone) 70%);
  }
  .card__chevron { position: absolute; left: 0; top: 0; width: 300px; height: 526px; }

  .brand {
    position: absolute; left: 0; right: 0; top: 318px;
    text-align: center;
    font-family: "Bebas Neue", sans-serif;
    font-size: 54px; line-height: 1;
    letter-spacing: 3px;
    color: var(--ink);
  }
  .brand__tagline {
    position: absolute; left: 0; right: 0; top: 380px;
    text-align: center;
    font-family: "Bebas Neue", sans-serif;
    font-size: 11px; letter-spacing: 0.3px;
    color: var(--ink);
  }

  .person__name {
    position: absolute; left: 0; right: 0; top: 242px;
    text-align: center;
    font-family: "Open Sans", sans-serif;
    font-size: 37px; line-height: 1; letter-spacing: -0.5px;
    color: var(--ink);
  }
  .person__role {
    position: absolute; left: 0; right: 0; top: 286px;
    text-align: center;
    font-family: "Open Sans", sans-serif;
    font-size: 18px; line-height: 1;
    color: var(--muted);
  }

  .contact__tab {
    position: absolute; width: 59px; height: 48px;
    background: var(--ink);
    display: flex; align-items: center; justify-content: center;
  }
  .contact__tab--left  { left: 0;  border-radius: 0 9px 9px 0; }
  .contact__tab--right { right: 0; border-radius: 9px 0 0 9px; }
  .contact__tab svg { width: 30px; height: 30px; }

  .contact__text {
    position: absolute;
    font-family: "Open Sans", sans-serif;
    font-size: 10.5px; line-height: 1;
    color: var(--ink);
    white-space: nowrap;
  }
  .contact__text--right { text-align: right; right: 68px; }
</style>
</head>
<body>
<div class="canvas">

  <section class="card card--front">
    <div class="card__texture" role="img" aria-label="Cream sandstone texture with faint cracked veining"></div>
    <svg class="card__chevron" viewBox="0 0 300 526" aria-hidden="true">
      <polygon points="0,-24 150,126 150,148 0,-2" fill="var(--band-light)"/>
      <polygon points="150,126 300,-24 300,-2 150,148" fill="var(--band-dark)"/>
      <polygon points="0,31 150,181 150,206 0,56" fill="var(--band-charcoal)"/>
      <polygon points="150,181 300,31 300,56 150,206" fill="var(--ink)"/>
    </svg>
    <h1 class="brand">QUELVADINE</h1>
    <p class="brand__tagline">SANDBLASTED STONE ✲ CULTURED STONE ✲ BRICK NATURAL STONE</p>
  </section>

  <section class="card card--back">
    <div class="card__texture" role="img" aria-label="Cream sandstone texture with faint cracked veining"></div>
    <svg class="card__chevron" viewBox="0 0 300 526" aria-hidden="true">
      <polygon points="0,-24 150,126 150,148 0,-2" fill="var(--band-light)"/>
      <polygon points="150,126 300,-24 300,-2 150,148" fill="var(--band-dark)"/>
      <polygon points="0,31 150,181 150,206 0,56" fill="var(--band-charcoal)"/>
      <polygon points="150,181 300,31 300,56 150,206" fill="var(--ink)"/>
    </svg>

    <h2 class="person__name">JANE ROWE</h2>
    <p class="person__role">Owner</p>

    <div class="contact__tab contact__tab--left" style="top:345px;">
      <svg viewBox="0 0 24 24" aria-label="Phone"><path fill="var(--icon)" d="M20 4c-2-1.5-4.5-1-4.8-.6l-1.6 2.8c-.2.4 0 .9.4 1.1l2 1.2c-.8 2-2.6 4.1-4.6 5.3l-1.3-1.9c-.3-.4-.8-.5-1.2-.3L6.2 13.3c-.4.3-.8 2.8.7 4.8C12.5 16 18 10.5 20 4z"/></svg>
    </div>
    <p class="contact__text" style="left:68px; top:362px;">555.010.4821</p>

    <div class="contact__tab contact__tab--right" style="top:370px;">
      <svg viewBox="0 0 24 24" aria-label="Website"><g fill="none" stroke="var(--icon)" stroke-width="1.6"><circle cx="12" cy="12" r="9"/><ellipse cx="12" cy="12" rx="4" ry="9"/><line x1="3" y1="12" x2="21" y2="12"/><path d="M5 7h14M5 17h14"/></g></svg>
    </div>
    <p class="contact__text contact__text--right" style="top:388px;">www.quelvadine-stone.com</p>

    <div class="contact__tab contact__tab--left" style="top:410px;">
      <svg viewBox="0 0 24 24" aria-label="Email"><g fill="none" stroke="var(--icon)" stroke-width="1.6"><rect x="2.5" y="5.5" width="19" height="13"/><path d="M2.5 5.5 12 13l9.5-7.5M2.5 18.5l7-6M21.5 18.5l-7-6"/></g></svg>
    </div>
    <p class="contact__text" style="left:67px; top:428px;">jane.rowe@quelvadine-stone.com</p>

    <div class="contact__tab contact__tab--right" style="top:438px;">
      <svg viewBox="0 0 24 24" aria-label="Address"><path fill="var(--icon)" d="M12 3 2 12h3v9h5v-6h4v6h5v-9h3L18 8.4V4h-2.5v2.2z"/></svg>
    </div>
    <p class="contact__text contact__text--right" style="top:455px;">Here goes your address</p>
  </section>

</div>
</body>
</html>
```